QuillMark Business Cards

I need a business card designed for QuillMark. To get an idea of what we do please visit https://formvault.example/para-creadores-3

```html
<!DOCTYPE html>
<html lang="en">
<head>
<meta charset="utf-8">
<title>QuillMark Business Cards</title>
<link rel="stylesheet" href="https://fonts.googleapis.com/css2?family=Montserrat:wght@300;400;500&display=swap">
<style>
  :root {
    --backdrop: #2b2b2b;
    --amber: #d4871a;
    --amber-deep: #c27812;
    --paper: #f1f1f0;
    --ink: #1c1c1f;
    --shadow-band: #17171b;
    --white: #ffffff;
  }
  * { margin: 0; padding: 0; box-sizing: border-box; }
  html, body {
    width: 1200px; height: 1138px; overflow: hidden;
    background: var(--backdrop);
    font-family: "Montserrat", sans-serif;
  }
  .canvas { position: relative; width: 1200px; height: 1138px; }

  .card {
    position: absolute;
    width: 620px; height: 375px;
    border-radius: 16px;
    overflow: hidden;
    box-shadow: 0 6px 14px rgba(0,0,0,.45);
  }

  /* Front */
  .card-front {
    left: 274px; top: 186px;
    background: linear-gradient(160deg, var(--amber) 0%, var(--amber-deep) 100%);
  }
  .card-front .wordmark {
    position: absolute; left: 43px; top: 280px;
    font-size: 33px; font-weight: 300; letter-spacing: 10px;
    color: var(--white); line-height: 1;
  }
  .card-front .tagline-row {
    position: absolute; left: 44px; top: 318px; width: 260px;
    display: flex; align-items: center; gap: 4px;
  }
  .tagline {
    font-size: 9px; font-weight: 400; letter-spacing: 5px; white-space: nowrap;
  }
  .card-front .tagline { color: var(--white); }
  .tagline-rule { flex: 1; height: 1px; }
  .card-front .tagline-rule { background: rgba(255,255,255,.75); }

  /* Back */
  .card-back {
    left: 276px; top: 608px;
    background: var(--paper);
  }
  .card-back .panel { position: absolute; left: 0; top: 0; }
  .card-back .brand {
    position: absolute; right: 26px; top: 48px; width: 300px;
  }
  .card-back .wordmark {
    text-align: right;
    font-size: 35px; font-weight: 400; letter-spacing: 9px; margin-right: -9px;
    color: var(--ink); line-height: 1;
  }
  .card-back .tagline-row {
    display: flex; align-items: center; gap: 12px; margin-top: 10px;
  }
  .card-back .tagline { color: var(--amber); }
  .card-back .tagline-rule { background: var(--ink); }

  .person { position: absolute; right: 28px; top: 152px; text-align: right; }
  .person-name { font-size: 27px; font-weight: 400; color: var(--amber); line-height: 1.1; }
  .person-role { font-size: 16px; font-weight: 400; color: var(--ink); margin-top: 6px; }

  .contacts {
    position: absolute; right: 28px; top: 242px;
    list-style: none; text-align: right;
    font-size: 15.5px; color: var(--ink);
  }
  .contacts li { display: flex; justify-content: flex-end; align-items: center; height: 26px; }
  .contacts li .icon { width: 16px; height: 16px; margin-left: 15px; }
  .contacts li.address { margin-top: 4px; }
</style>
</head>
<body>
<main class="canvas">

  <section class="card card-front" aria-label="Card front">
    <div class="wordmark">QUILLMARK</div>
    <div class="tagline-row">
      <span class="tagline">DIGITAL NOTARY</span>
      <span class="tagline-rule"></span>
    </div>
  </section>

  <section class="card card-back" aria-label="Card back">
    <svg class="panel" width="620" height="375" viewBox="0 0 620 375" aria-hidden="true">
      <path d="M0 0 H222 Q298 190 214 375 H0 Z" fill="var(--shadow-band)"/>
      <path d="M0 0 H216 Q288 190 203 375 H0 Z" fill="var(--amber)"/>
    </svg>

    <div class="brand">
      <div class="wordmark">QUILLMARK</div>
      <div class="tagline-row">
        <span class="tagline">DIGITAL NOTARY</span>
        <span class="tagline-rule"></span>
      </div>
    </div>

    <div class="person">
      <div class="person-name">Dana Whitlow</div>
      <div class="person-role">President</div>
    </div>

    <ul class="contacts">
      <li>000-0000-0000
        <svg class="icon" viewBox="0 0 16 16" aria-hidden="true"><path d="M2 6c0-2 2.5-3 6-3s6 1 6 3v1h-3V5.5H5V7H2z M4 8h8l1.5 5h-11z" fill="var(--amber)"/></svg>
      </li>
      <li>dana@quillmark.example
        <svg class="icon" viewBox="0 0 16 16" aria-hidden="true"><rect x="1.5" y="3.5" width="13" height="9" fill="var(--amber)"/><path d="M1.5 3.5 L8 9 L14.5 3.5 M1.5 12.5 L6 8 M14.5 12.5 L10 8" stroke="var(--paper)" stroke-width="1" fill="none"/></svg>
      </li>
      <li>www.quillmark.example
        <svg class="icon" viewBox="0 0 16 16" aria-hidden="true"><g fill="none" stroke="var(--amber)" stroke-width="1.3"><circle cx="8" cy="8" r="6"/><ellipse cx="8" cy="8" rx="2.6" ry="6"/><path d="M2 8h12M3 5h10M3 11h10"/></g></svg>
      </li>
      <li class="address">Millbrook Harbor, Minnesota, US</li>
    </ul>
  </section>

</main>
</body>
</html>
```